Velvet Oaks rebranding my business with a new business card

I have my new logo and now I need a refresher on my business cards. I really want something fun and fresh. I like black background or anything to make the color pop.
Logo
Name: Velvet Oaks
Contact Info as stated below:
Mira Calloway
647-382-9164
Logo
Name: Velvet Oaks
Mira Calloway
647-382-9164
fb.me/VelvetOaksbyMira
Instagram: @VelvetOaksbyMira

Industry/Entity Type

Business

Contact Information for Business Card

double-sided. Logo on one side. Contact info on the other.

Requirements
Must have
• Logo
• Name: Velvet Oaks
• Contact Info as stated below:
• Mira Calloway
• 647-382-9164
• fb.me/VelvetOaksbyMira
• fb.me/VelvetOaksbyMira

```html
<!DOCTYPE html>
<html lang="en">
<head>
<meta charset="utf-8">
<title>Velvet Oaks — Business Card</title>
<link rel="stylesheet" href="https://fonts.googleapis.com/css2?family=Lato:wght@300;400;700&family=Quicksand:wght@300;700&display=swap">
<style>
  :root {
    --ink: #000000;
    --cream: #efe2b6;
    --paper: #ffffff;
    --text: #1c1c1c;
    --rose: #f2a9c4;
    --backdrop: #d9dadd;
  }
  * { box-sizing: border-box; margin: 0; padding: 0; }
  html, body { width: 1200px; height: 1200px; overflow: hidden; }
  body {
    background: var(--backdrop);
    display: flex;
    flex-direction: column;
    align-items: center;
    justify-content: center;
    gap: 60px;
    font-family: "Lato", sans-serif;
  }
  .card {
    position: relative;
    width: 840px;
    height: 480px;
    overflow: hidden;
    box-shadow: 0 10px 30px rgba(0,0,0,0.18);
  }

  /* Logo badge shared by both sides */
  .logo-badge {
    position: absolute;
    width: 220px;
    height: 220px;
    border-radius: 50%;
    background: var(--paper);
    box-shadow: inset 0 0 0 7px var(--paper), inset 0 0 0 9px var(--rose);
    display: flex;
    align-items: center;
    justify-content: center;
    z-index: 3;
  }
  .logo-name {
    font-family: "Lato", sans-serif;
    font-weight: 700;
    font-size: 28px;
    color: var(--text);
    letter-spacing: 0.5px;
  }

  /* Front */
  .card-front { background: var(--ink); }
  .card-front .band {
    position: absolute;
    left: 0; right: 0;
    top: 185px;
    height: 90px;
    background: var(--cream);
  }
  .card-front .logo-badge { left: 310px; top: 120px; }

  /* Back */
  .card-back { background: var(--paper); }
  .card-back .name-band {
    position: absolute;
    left: 0; right: 0;
    top: 140px;
    height: 86px;
    background: var(--cream);
    z-index: 0;
  }
  .card-back .edge {
    position: absolute;
    inset: 0;
    background: var(--cream);
    clip-path: polygon(0 0, 540px 0, 318px 480px, 0 480px);
    z-index: 1;
  }
  .card-back .panel {
    position: absolute;
    inset: 0;
    background: var(--ink);
    clip-path: polygon(0 0, 528px 0, 306px 480px, 0 480px);
    z-index: 2;
  }
  .card-back .logo-badge { left: 145px; top: 70px; }

  .person-name {
    position: absolute;
    right: 46px;
    top: 140px;
    height: 86px;
    display: flex;
    align-items: center;
    font-family: "Quicksand", sans-serif;
    font-size: 40px;
    color: var(--text);
    z-index: 3;
  }
  .person-name .first { font-weight: 700; margin-right: 10px; }
  .person-name .last { font-weight: 300; }

  .contact-list {
    position: absolute;
    right: 46px;
    top: 282px;
    list-style: none;
    text-align: right;
    z-index: 3;
  }
  .contact-item {
    display: flex;
    justify-content: flex-end;
    align-items: center;
    gap: 10px;
    font-size: 22px;
    font-weight: 400;
    color: var(--text);
    line-height: 34px;
  }
  .contact-icon { width: 18px; height: 18px; flex: none; }
</style>
</head>
<body>

  <section class="card card-front" aria-label="Card front">
    <div class="band"></div>
    <div class="logo-badge"><span class="logo-name">Velvet Oaks</span></div>
  </section>

  <section class="card card-back" aria-label="Card back">
    <div class="name-band"></div>
    <div class="edge"></div>
    <div class="panel"></div>
    <div class="logo-badge"><span class="logo-name">Velvet Oaks</span></div>

    <h1 class="person-name"><span class="first">Mira</span><span class="last">Calloway</span></h1>

    <ul class="contact-list">
      <li class="contact-item">647-382-9164
        <svg class="contact-icon" viewBox="0 0 24 24" aria-hidden="true"><path fill="#1c1c1c" d="M6.6 10.8a15.1 15.1 0 0 0 6.6 6.6l2.2-2.2c.3-.3.7-.4 1-.2 1.1.4 2.3.6 3.6.6.6 0 1 .4 1 1V20c0 .6-.4 1-1 1A17 17 0 0 1 3 4c0-.6.4-1 1-1h3.5c.6 0 1 .4 1 1 0 1.3.2 2.5.6 3.6.1.3 0 .7-.2 1z"/></svg>
      </li>
      <li class="contact-item">info@VelvetOaks.com
        <svg class="contact-icon" viewBox="0 0 24 24" aria-hidden="true"><rect x="2" y="5" width="20" height="14" rx="2" fill="#1c1c1c"/><path d="M3 6l9 7 9-7" fill="none" stroke="#fff" stroke-width="1.6"/></svg>
      </li>
      <li class="contact-item">www.VelvetOaks.com
        <svg class="contact-icon" viewBox="0 0 24 24" aria-hidden="true"><circle cx="12" cy="12" r="10" fill="#1c1c1c"/><g fill="none" stroke="#fff" stroke-width="1.3"><ellipse cx="12" cy="12" rx="4" ry="10"/><path d="M2 12h20M4 7h16M4 17h16"/></g></svg>
      </li>
      <li class="contact-item">fb.me/VelvetOaksbyMira
        <svg class="contact-icon" viewBox="0 0 24 24" aria-hidden="true"><circle cx="12" cy="12" r="10" fill="#1c1c1c"/></svg>
      </li>
    </ul>
  </section>

</body>
</html>
```